social interest sharing site needs a web site design

we need a web site design for a social web platform.
the site is one page(main page), that is split into 3 sections
each section is a different color(red,green and blue)
and a user can choose to share each of the sections.
any section/color will contain boxes , each box can contain different media types.

the media types:
* list of URLS
* list of articles including title + image + description
* list of videos
* thumbnails of images
* calender
* list of emails

the main content will look like corkboardly layout
multiple boxes each box can contain different type of content as described above

each color is a different tab
each tab will have layout like corkboardly
Updates

please read the last description update.
and i uploaded an image that can explain the requirements better

thanks
Oren
 

Industry/Entity Type

Media

```html
<!DOCTYPE html>
<html lang="en">
<head>
<meta charset="utf-8">
<title>Plinkit.me</title>
<link href="https://fonts.googleapis.com/css2?family=Open+Sans:wght@400;600;700&family=Ubuntu:wght@500&display=swap" rel="stylesheet">
<style>
:root{
  --red:#fd7672;
  --green:#3ecfb0;
  --blue:#5aa2df;
  --tab-blue:#4a8fd0;
  --navy:#3c5a86;
  --page:#efefef;
  --panel:#ffffff;
  --footer:#c8c8c8;
  --ink:#555b60;
  --muted:#a9aeb2;
  --rule:#e2e2e2;
}
*{box-sizing:border-box;margin:0;padding:0}
html,body{width:1200px;height:1108px;overflow:hidden}
body{position:relative;background:var(--page);font-family:"Open Sans",sans-serif;color:var(--ink)}
.topbar{position:absolute;left:0;top:0;width:1200px;height:41px;background:#f3f3f3}
.band{position:absolute;left:0;top:41px;width:1200px;height:91px;background:var(--blue)}
.sec{position:absolute;top:0;height:132px}
.sec-red{left:0;width:204px;background:var(--red)}
.sec-green{left:204px;width:72px;background:var(--green)}
.sec-label{position:absolute;top:106px;font-size:9.5px;line-height:12px;color:#fff}
.brand{position:absolute;left:180px;top:56px;font-size:36px;font-weight:700;color:#fff;letter-spacing:-1px}
.following{position:absolute;left:556px;top:8px;font-size:11px;font-weight:700;line-height:12px;color:#111}
.quick{position:absolute;top:6px;width:117px;height:29px;background:var(--navy);border:1px solid #2e4a70;border-radius:4px;
  box-shadow:inset 0 1px 0 rgba(255,255,255,.25);color:#fff;font-size:9px;font-weight:700;line-height:9.5px;padding:5px 6px;letter-spacing:.3px}
.tabs{position:absolute;left:342px;top:93px;width:678px;height:39px;background:var(--tab-blue);border-radius:6px 6px 0 0;display:flex}
.tab{font-family:"Ubuntu",sans-serif;font-size:12.5px;font-weight:500;color:#fff;padding:15px 10px 0;white-space:nowrap;position:relative}
.tab.active{background:var(--red);border-radius:6px 6px 0 0;margin-top:-7px;padding-top:22px}
.tab.active::after{content:"";position:absolute;left:50%;bottom:0;margin-left:-6px;border:6px solid transparent;border-bottom-color:var(--panel)}
.panel{position:absolute;left:120px;top:132px;width:914px;height:907px;background:var(--panel)}
.footer{position:absolute;left:0;top:1039px;width:1200px;height:69px;background:var(--footer)}
.grid{position:absolute;left:134px;top:148px;display:grid;grid-template-columns:repeat(4,209px);column-gap:16px;row-gap:15px}
.card{width:209px;height:277px;background:#fff;border-bottom:4px solid #dedede;box-shadow:0 0 3px rgba(0,0,0,.18)}
.card.hot{border-bottom-color:#fcc4c2;box-shadow:0 0 3px rgba(253,118,114,.45)}
.thumb{height:174px;background:radial-gradient(ellipse at 55% 45%,#e6eaec 0 32%,#b9b7ae 46%,#8f6f52 70%,#4b3a30 100%)}
.excerpt{font-size:11px;line-height:15px;text-align:center;padding:6px 10px 0;height:60px;color:#666}
.meta{margin:0 6px;border-top:1px solid var(--rule);height:39px;display:flex;align-items:center}
.avatar{width:28px;height:28px;border-radius:2px;background:linear-gradient(#ffd21e,#f2a800);flex:none}
.author{margin-left:6px;font-size:11px;line-height:14px}
.author b{font-weight:600;color:#333}
.author span{display:block;color:var(--muted)}
.stats{margin-left:auto;display:flex;gap:9px;font-size:10px;color:#a9885a;align-items:center}
.stats svg{vertical-align:-1px;margin-right:2px}
</style>
</head>
<body>
<div class="topbar"></div>
<div class="band"></div>
<div class="sec sec-red"></div>
<div class="sec sec-green"></div>
<div class="sec-label" style="left:134px">My home<br>page</div>
<div class="sec-label" style="left:209px">My favorites<br>videos</div>
<div class="sec-label" style="left:282px">Personal<br>apps</div>
<div class="brand">Plinkit.me</div>

<div class="following">Following<br>PLINKIT</div>
<div class="quick" style="left:627px">Danas favorites<br>Videos</div>
<div class="quick" style="left:761px">Mayas pics +<br>favorites links</div>
<div class="quick" style="left:895px">Familiy weekly<br>calendar and notes</div>

<nav class="tabs">
  <div class="tab">LIST OF URLS</div>
  <div class="tab active">LIST OF ARTICLES</div>
  <div class="tab">LIST OF VIDEOS</div>
  <div class="tab">THUMBNAILS OF IMAGES</div>
  <div class="tab">CALENDERV</div>
  <div class="tab">LIST OF EMAILS</div>
</nav>

<main class="panel"></main>

<section class="grid">
  <!-- rows of article cards -->
  <article class="card hot"><div class="thumb" role="img" aria-label="Article image: app screen over a blurred photo"></div><p class="excerpt">Quisque id tellus quis risus vehicula vehicula ut turpis. In eros nulla Quisque id tellus quis risus vehicula</p><div class="meta"><div class="avatar" role="img" aria-label="Author avatar"></div><div class="author"><b>Tomás Ribeiro</b><span>Identidade</span></div><div class="stats"><span><svg width="10" height="10" viewBox="0 0 10 10"><path d="M3 1h4v1H6v3l2 2H2l2-2V2H3zM5 7v3" stroke="#bbb" fill="none"/></svg>8</span><span><svg width="11" height="10" viewBox="0 0 11 10"><path d="M5.5 9.5L1 5a2.5 2.5 0 0 1 4.5-3.2A2.5 2.5 0 0 1 10 5z" fill="#ccc"/></svg>4</span></div></div></article>
  <article class="card"><div class="thumb" role="img" aria-label="Article image: app screen over a blurred photo"></div><p class="excerpt">Quisque id tellus quis risus vehicula vehicula ut turpis. In eros nulla Quisque id tellus quis risus vehicula</p><div class="meta"><div class="avatar" role="img" aria-label="Author avatar"></div><div class="author"><b>Tomás Ribeiro</b><span>Identidade</span></div><div class="stats"><span><svg width="10" height="10" viewBox="0 0 10 10"><path d="M3 1h4v1H6v3l2 2H2l2-2V2H3zM5 7v3" stroke="#bbb" fill="none"/></svg>8</span><span><svg width="11" height="10" viewBox="0 0 11 10"><path d="M5.5 9.5L1 5a2.5 2.5 0 0 1 4.5-3.2A2.5 2.5 0 0 1 10 5z" fill="#ccc"/></svg>4</span></div></div></article>
  <article class="card"><div class="thumb" role="img" aria-label="Article image: app screen over a blurred photo"></div><p class="excerpt">Quisque id tellus quis risus vehicula vehicula ut turpis. In eros nulla Quisque id tellus quis risus vehicula</p><div class="meta"><div class="avatar" role="img" aria-label="Author avatar"></div><div class="author"><b>Tomás Ribeiro</b><span>Identidade</span></div><div class="stats"><span><svg width="10" height="10" viewBox="0 0 10 10"><path d="M3 1h4v1H6v3l2 2H2l2-2V2H3zM5 7v3" stroke="#bbb" fill="none"/></svg>8</span><span><svg width="11" height="10" viewBox="0 0 11 10"><path d="M5.5 9.5L1 5a2.5 2.5 0 0 1 4.5-3.2A2.5 2.5 0 0 1 10 5z" fill="#ccc"/></svg>4</span></div></div></article>
  <article class="card"><div class="thumb" role="img" aria-label="Article image: app screen over a blurred photo"></div><p class="excerpt">Quisque id tellus quis risus vehicula vehicula ut turpis. In eros nulla Quisque id tellus quis risus vehicula</p><div class="meta"><div class="avatar" role="img" aria-label="Author avatar"></div><div class="author"><b>Tomás Ribeiro</b><span>Identidade</span></div><div class="stats"><span><svg width="10" height="10" viewBox="0 0 10 10"><path d="M3 1h4v1H6v3l2 2H2l2-2V2H3zM5 7v3" stroke="#bbb" fill="none"/></svg>8</span><span><svg width="11" height="10" viewBox="0 0 11 10"><path d="M5.5 9.5L1 5a2.5 2.5 0 0 1 4.5-3.2A2.5 2.5 0 0 1 10 5z" fill="#ccc"/></svg>4</span></div></div></article>

  <article class="card hot"><div class="thumb" role="img" aria-label="Article image: app screen over a blurred photo"></div><p class="excerpt">Quisque id tellus quis risus vehicula vehicula ut turpis. In eros nulla Quisque id tellus quis risus vehicula</p><div class="meta"><div class="avatar" role="img" aria-label="Author avatar"></div><div class="author"><b>Tomás Ribeiro</b><span>Identidade</span></div><div class="stats"><span><svg width="10" height="10" viewBox="0 0 10 10"><path d="M3 1h4v1H6v3l2 2H2l2-2V2H3zM5 7v3" stroke="#bbb" fill="none"/></svg>8</span><span><svg width="11" height="10" viewBox="0 0 11 10"><path d="M5.5 9.5L1 5a2.5 2.5 0 0 1 4.5-3.2A2.5 2.5 0 0 1 10 5z" fill="#ccc"/></svg>4</span></div></div></article>
  <article class="card"><div class="thumb" role="img" aria-label="Article image: app screen over a blurred photo"></div><p class="excerpt">Quisque id tellus quis risus vehicula vehicula ut turpis. In eros nulla Quisque id tellus quis risus vehicula</p><div class="meta"><div class="avatar" role="img" aria-label="Author avatar"></div><div class="author"><b>Tomás Ribeiro</b><span>Identidade</span></div><div class="stats"><span><svg width="10" height="10" viewBox="0 0 10 10"><path d="M3 1h4v1H6v3l2 2H2l2-2V2H3zM5 7v3" stroke="#bbb" fill="none"/></svg>8</span><span><svg width="11" height="10" viewBox="0 0 11 10"><path d="M5.5 9.5L1 5a2.5 2.5 0 0 1 4.5-3.2A2.5 2.5 0 0 1 10 5z" fill="#ccc"/></svg>4</span></div></div></article>
  <article class="card"><div class="thumb" role="img" aria-label="Article image: app screen over a blurred photo"></div><p class="excerpt">Quisque id tellus quis risus vehicula vehicula ut turpis. In eros nulla Quisque id tellus quis risus vehicula</p><div class="meta"><div class="avatar" role="img" aria-label="Author avatar"></div><div class="author"><b>Tomás Ribeiro</b><span>Identidade</span></div><div class="stats"><span><svg width="10" height="10" viewBox="0 0 10 10"><path d="M3 1h4v1H6v3l2 2H2l2-2V2H3zM5 7v3" stroke="#bbb" fill="none"/></svg>8</span><span><svg width="11" height="10" viewBox="0 0 11 10"><path d="M5.5 9.5L1 5a2.5 2.5 0 0 1 4.5-3.2A2.5 2.5 0 0 1 10 5z" fill="#ccc"/></svg>4</span></div></div></article>
  <article class="card"><div class="thumb" role="img" aria-label="Article image: app screen over a blurred photo"></div><p class="excerpt">Quisque id tellus quis risus vehicula vehicula ut turpis. In eros nulla Quisque id tellus quis risus vehicula</p><div class="meta"><div class="avatar" role="img" aria-label="Author avatar"></div><div class="author"><b>Tomás Ribeiro</b><span>Identidade</span></div><div class="stats"><span><svg width="10" height="10" viewBox="0 0 10 10"><path d="M3 1h4v1H6v3l2 2H2l2-2V2H3zM5 7v3" stroke="#bbb" fill="none"/></svg>8</span><span><svg width="11" height="10" viewBox="0 0 11 10"><path d="M5.5 9.5L1 5a2.5 2.5 0 0 1 4.5-3.2A2.5 2.5 0 0 1 10 5z" fill="#ccc"/></svg>4</span></div></div></article>

  <article class="card hot"><div class="thumb" role="img" aria-label="Article image: app screen over a blurred photo"></div><p class="excerpt">Quisque id tellus quis risus vehicula vehicula ut turpis. In eros nulla Quisque id tellus quis risus vehicula</p><div class="meta"><div class="avatar" role="img" aria-label="Author avatar"></div><div class="author"><b>Tomás Ribeiro</b><span>Identidade</span></div><div class="stats"><span><svg width="10" height="10" viewBox="0 0 10 10"><path d="M3 1h4v1H6v3l2 2H2l2-2V2H3zM5 7v3" stroke="#bbb" fill="none"/></svg>8</span><span><svg width="11" height="10" viewBox="0 0 11 10"><path d="M5.5 9.5L1 5a2.5 2.5 0 0 1 4.5-3.2A2.5 2.5 0 0 1 10 5z" fill="#ccc"/></svg>4</span></div></div></article>
  <article class="card"><div class="thumb" role="img" aria-label="Article image: app screen over a blurred photo"></div><p class="excerpt">Quisque id tellus quis risus vehicula vehicula ut turpis. In eros nulla Quisque id tellus quis risus vehicula</p><div class="meta"><div class="avatar" role="img" aria-label="Author avatar"></div><div class="author"><b>Tomás Ribeiro</b><span>Identidade</span></div><div class="stats"><span><svg width="10" height="10" viewBox="0 0 10 10"><path d="M3 1h4v1H6v3l2 2H2l2-2V2H3zM5 7v3" stroke="#bbb" fill="none"/></svg>8</span><span><svg width="11" height="10" viewBox="0 0 11 10"><path d="M5.5 9.5L1 5a2.5 2.5 0 0 1 4.5-3.2A2.5 2.5 0 0 1 10 5z" fill="#ccc"/></svg>4</span></div></div></article>
  <article class="card"><div class="thumb" role="img" aria-label="Article image: app screen over a blurred photo"></div><p class="excerpt">Quisque id tellus quis risus vehicula vehicula ut turpis. In eros nulla Quisque id tellus quis risus vehicula</p><div class="meta"><div class="avatar" role="img" aria-label="Author avatar"></div><div class="author"><b>Tomás Ribeiro</b><span>Identidade</span></div><div class="stats"><span><svg width="10" height="10" viewBox="0 0 10 10"><path d="M3 1h4v1H6v3l2 2H2l2-2V2H3zM5 7v3" stroke="#bbb" fill="none"/></svg>8</span><span><svg width="11" height="10" viewBox="0 0 11 10"><path d="M5.5 9.5L1 5a2.5 2.5 0 0 1 4.5-3.2A2.5 2.5 0 0 1 10 5z" fill="#ccc"/></svg>4</span></div></div></article>
  <article class="card"><div class="thumb" role="img" aria-label="Article image: app screen over a blurred photo"></div><p class="excerpt">Quisque id tellus quis risus vehicula vehicula ut turpis. In eros nulla Quisque id tellus quis risus vehicula</p><div class="meta"><div class="avatar" role="img" aria-label="Author avatar"></div><div class="author"><b>Tomás Ribeiro</b><span>Identidade</span></div><div class="stats"><span><svg width="10" height="10" viewBox="0 0 10 10"><path d="M3 1h4v1H6v3l2 2H2l2-2V2H3zM5 7v3" stroke="#bbb" fill="none"/></svg>8</span><span><svg width="11" height="10" viewBox="0 0 11 10"><path d="M5.5 9.5L1 5a2.5 2.5 0 0 1 4.5-3.2A2.5 2.5 0 0 1 10 5z" fill="#ccc"/></svg>4</span></div></div></article>
</section>

<div class="footer"></div>
</body>
</html>
```